We need a full corporate logo and stationary design for our business oxForge. OxForge provides 3D Printing Services to the Australian Market.

Our predominant market is the Mining and Architectural industries and our secondary market is the Entrepreneur / Start-up sector.

What we are after:

1. Logo
2. Business Card Design
3. Letterhead Design
4. Email Signature Design

File Formats we require in colour, greyscale and Black and White:

1 .AI
2 .EPS
3 .TIF
4 .PDF
5 .PNG (300 dpi)
6 .JPG (300 dpi)
7 .GIF (300 dpi)

• Should Not Have:
- "Clip-Art" should not be used.

```html
<!DOCTYPE html>
<html lang="en">
<head>
<meta charset="utf-8">
<title>oxForge Australia — Envelope</title>
<link href="https://fonts.googleapis.com/css2?family=Open+Sans:wght@400;700&display=swap" rel="stylesheet">
<style>
  :root {
    --page: #ffffff;
    --paper-light: #ffffff;
    --paper-edge: #e4e5e7;
    --flap-edge: #dfe0e2;
    --brand-deep: #3b3f9e;
    --brand-bright: #08a8e6;
    --stripe: #0fa9ea;
    --ink-dark: #333333;
    --ink-light: #ffffff;
    --dieline: #6d6e70;
  }
  html, body {
    margin: 0;
    padding: 0;
    overflow: hidden;
    background: var(--page);
  }
  .canvas {
    width: 1200px;
    height: 1060px;
    position: relative;
    overflow: hidden;
  }
  .envelope-art {
    display: block;
    width: 1200px;
    height: 1060px;
  }
  .brand-name {
    font-family: "Open Sans", Arial, sans-serif;
    font-weight: 700;
    font-size: 35px;
    fill: var(--ink-dark);
  }
  .web-address {
    font-family: "Open Sans", Arial, sans-serif;
    font-weight: 700;
    font-size: 25px;
    fill: var(--ink-light);
  }
  .contact-line {
    font-family: "Open Sans", Arial, sans-serif;
    font-weight: 400;
    font-size: 11.5px;
    fill: var(--ink-light);
  }
  .contact-email {
    font-family: "Open Sans", Arial, sans-serif;
    font-weight: 400;
    font-size: 14px;
    fill: var(--ink-light);
  }
  .contact-icon {
    fill: var(--ink-light);
  }
</style>
</head>
<body>
<div class="canvas">
  <svg class="envelope-art" viewBox="0 0 1200 1060" xmlns="http://www.w3.org/2000/svg">
    <defs>
      <radialGradient id="flapGradient" cx="0.5" cy="0.35" r="0.6">
        <stop offset="0" stop-color="var(--brand-bright)"/>
        <stop offset="1" stop-color="var(--brand-deep)"/>
      </radialGradient>
      <radialGradient id="paperGradient" cx="0.5" cy="0.5" r="0.65">
        <stop offset="0" stop-color="var(--paper-light)"/>
        <stop offset="1" stop-color="var(--paper-edge)"/>
      </radialGradient>
      <linearGradient id="sideFlapGradient" x1="0" y1="0" x2="0" y2="1">
        <stop offset="0" stop-color="var(--flap-edge)"/>
        <stop offset="0.5" stop-color="var(--paper-light)"/>
        <stop offset="1" stop-color="var(--flap-edge)"/>
      </linearGradient>
      <linearGradient id="bandGradient" x1="0" y1="0" x2="1" y2="0">
        <stop offset="0" stop-color="var(--brand-deep)"/>
        <stop offset="0.8" stop-color="var(--brand-bright)"/>
        <stop offset="1" stop-color="#1d8fd8"/>
      </linearGradient>
    </defs>

    <!-- side flaps -->
    <rect class="side-flap side-flap--left" x="0.5" y="176" width="56" height="500" fill="url(#sideFlapGradient)" stroke="var(--dieline)" stroke-width="1"/>
    <rect class="side-flap side-flap--right" x="1142" y="176" width="57.5" height="500" fill="url(#sideFlapGradient)" stroke="var(--dieline)" stroke-width="1"/>

    <!-- bottom flap -->
    <polygon class="bottom-flap" points="56,676 1142,676 1114,1059 88,1059" fill="url(#paperGradient)" stroke="var(--dieline)" stroke-width="1"/>

    <!-- top flap -->
    <path class="top-flap" d="M56,176 L56,72 Q56,0 128,0 L1070,0 Q1142,0 1142,72 L1142,176 Z" fill="url(#flapGradient)"/>
    <text class="web-address" x="0" y="0" text-anchor="middle" transform="translate(600,80) rotate(180)">www.oxforge.com</text>

    <!-- front panel -->
    <rect class="front-panel" x="56" y="176" width="1086" height="500" fill="url(#paperGradient)"/>

    <!-- blue band with accent stripe -->
    <polygon class="accent-stripe" points="56,578 1142,500 1142,503 56,604" fill="var(--stripe)"/>
    <polygon class="contact-band" points="56,605 1142,503 1142,676 56,676" fill="url(#bandGradient)"/>

    <!-- brand -->
    <text class="brand-name" x="116" y="364">oxForge Australia</text>

    <!-- contact details -->
    <g class="contact-block">
      <text class="contact-line" x="1057" y="550" text-anchor="end">Address, street hgfg 789</text>
      <text class="contact-line" x="1057" y="565" text-anchor="end">jhjhgjhh jgjhgjh g</text>
      <path class="contact-icon icon-pin" d="M1070,535 a10,10 0 0 1 10,10 c0,8 -10,19 -10,19 c0,0 -10,-11 -10,-19 a10,10 0 0 1 10,-10 z M1070,540 a4.5,4.5 0 1 0 0.01,0 z" fill-rule="evenodd"/>

      <text class="contact-line" x="1057" y="595" text-anchor="end">(office) - (20) 123 4567 899</text>
      <text class="contact-line" x="1057" y="609" text-anchor="end">(mobile) - (20) 123 4567 899</text>
      <path class="contact-icon icon-phone" d="M1063,583 h16 a3,3 0 0 1 3,3 v26 a3,3 0 0 1 -3,3 h-16 a3,3 0 0 1 -3,-3 v-26 a3,3 0 0 1 3,-3 z M1063,588 v20 h16 v-20 z M1069,610 h4 v2 h-4 z" fill-rule="evenodd"/>

      <text class="contact-email" x="1057" y="640" text-anchor="end">yournameceo@oxforge.com</text>
      <g class="contact-icon icon-mail">
        <rect x="1060" y="625" width="25" height="17" fill="var(--ink-light)"/>
        <polyline points="1060,625 1072.5,635 1085,625" fill="none" stroke="#1b8fd6" stroke-width="1.5"/>
      </g>
    </g>

    <!-- dieline around front panel -->
    <rect class="dieline" x="56" y="176" width="1086" height="500" fill="none" stroke="var(--dieline)" stroke-width="1"/>
  </svg>
</div>
</body>
</html>
```